Tri-Fold Menu of Services for our Eyelash and Skin Care Spa

We need a beautiful spa service menu for our upscale spa in St. Charles Missouri. We specialize in providing treatments that are specific to the clients needs. Our services are eyelash extensions, skin care treatments, full body waxing and makeup application. Our spa colors are dark purples and greys and we are not opposed to additional colors that would complement those colors. We do a lot of eyelash extensions and while we do what those services listed we would like the skin care treatments to be in an area that would be noticed first. One of the attachments lists all of our services, descriptions and prices (please be sure to include all services and pricing. descriptions if possible). And our website has more information about us if needed. The website was not professionally done. So it DOESN'T represent our style exactly.

I HAVE ATTACHED A FEW PHOTOS BUT THEY DON'T HAVE TO BE USED.

Target Market(s)

women who would like to look their best, 35-55, annual income of 100,000+, she is usually busy and her children (if she has any) are high school age or older.

Industry/Entity Type

It Service

Font styles to use
Serif
Sans Serif

Requirements
Must have
• Must list all of our services. If it works to have the descriptions that would be great.
Nice to have
• If it works to have the descriptions of each service that would be great.

```html
<!DOCTYPE html>
<html lang="en">
<head>
<meta charset="utf-8">
<title>Velora Lash &amp; Skin Spa — Facial &amp; Skin Treatments</title>
<link rel="stylesheet" href="https://fonts.googleapis.com/css2?family=Source+Sans+3:wght@300;400&display=swap">
<style>
  :root {
    --heading: #3a1d3c;
    --price: #e3261d;
    --body: #4a4a4a;
    --bg-warm: #fdf6c4;
    --bg-cool: #e4f0e9;
    --photo-portrait-top: #efe6dd;
    --photo-portrait-bottom: #f6f1ea;
    --photo-brushes-top: #f1ebe2;
    --photo-brushes-bottom: #f7f3ec;
    --brand: #3a1d3c;
  }
  * { margin: 0; padding: 0; box-sizing: border-box; }
  html, body { width: 1200px; height: 938px; overflow: hidden; }
  body { font-family: "Source Sans 3", "Source Sans Pro", sans-serif; font-weight: 300; color: var(--body); }
  .menu-panel {
    position: relative; width: 1200px; height: 938px; overflow: hidden;
    background:
      radial-gradient(ellipse 700px 500px at 900px 80px, var(--bg-warm) 0%, rgba(253,246,196,0) 100%),
      linear-gradient(150deg, #fbfaf0 0%, #fbf8dc 45%, var(--bg-cool) 100%);
  }
  .column { position: absolute; top: 24px; z-index: 2; }
  .column--left { left: 28px; width: 374px; }
  .column--middle { left: 424px; width: 374px; }
  .column--right { left: 822px; width: 356px; }
  .service { margin-bottom: 23px; }
  .service-title {
    font-weight: 300; font-size: 25.5px; line-height: 32px; color: var(--heading);
    text-transform: uppercase;
  }
  .service-subtitle { font-weight: 400; font-size: 16.5px; line-height: 22px; color: var(--heading); margin-top: 0; }
  .service-price { font-weight: 300; font-size: 19.5px; line-height: 24px; color: var(--price); margin: 4px 0 6px; }
  .service-desc {
    font-size: 16.6px; line-height: 21.5px; text-align: justify; hyphens: auto; -webkit-hyphens: auto;
  }
  .photo {
    position: absolute; z-index: 1;
  }
  .photo--portrait {
    left: 820px; top: 385px; width: 380px; height: 553px;
    background: linear-gradient(180deg, var(--photo-portrait-top) 0%, var(--photo-portrait-bottom) 100%);
  }
  .photo--brushes {
    left: 470px; top: 648px; width: 340px; height: 290px;
    background: linear-gradient(180deg, var(--photo-brushes-top) 0%, var(--photo-brushes-bottom) 100%);
  }
  .brand {
    position: absolute; left: 980px; top: 842px; z-index: 3;
    font-weight: 400; font-size: 30px; line-height: 32px; color: var(--brand);
  }
  .brand-tag { display: block; font-size: 14px; line-height: 18px; }
</style>
</head>
<body>
<main class="menu-panel">
  <div class="photo photo--brushes" role="img" aria-label="Photo: hand holding a fan of makeup brushes"></div>
  <div class="photo photo--portrait" role="img" aria-label="Photo: portrait of a woman with sleek dark hair and bare shoulders"></div>

  <section class="column column--left">
    <article class="service">
      <h2 class="service-title">Facial &amp; Skin Treatments</h2>
      <p class="service-subtitle">Essential Deep Cleansing Treatment</p>
      <p class="service-price">$65 | 60 minutes</p>
      <p class="service-desc">This relaxing, purifying treatment consists of steaming, exfoliation, and an intense deeper cleansing of clogged pores. A skintype specific ampoule is gently massaged into the skin of your face, neck, and decollete, followed by a therapist selected mask. Beneficial for all skin types.</p>
    </article>
    <article class="service">
      <h2 class="service-title">Mini Facial</h2>
      <p class="service-price">$48 | 30 minutes</p>
      <p class="service-desc">This express facial is ideal for those on the go. Your skin is cleansed, lightly exfoliated and gently massaged. A porerefining mask is then applied, followed by a veil of light moisturizer</p>
    </article>
    <article class="service">
      <h2 class="service-title">Aromatherapy Facial</h2>
      <p class="service-price">$75 | 60 minutes</p>
      <p class="service-desc">Our Aromatherapy facial will naturally enhance the facial benefits using fragrant oils extracted from flowers, fruits and herbs.</p>
    </article>
    <article class="service">
      <h2 class="service-title">Firmlift Lift &amp;<br>Glow Treatment Facial</h2>
      <p class="service-price">$75 | 60 minutes</p>
      <p class="service-desc">Seeking a treatment with amazing instant results? Redefining radiance and facial contouring, this exclusively formulated treatment features the latest in freezedried technology to deliver instant results and cumulative skin care benefits. Ideal for any skin type showing signs of aging, or as the perfect instant repair boost when you want to look your best. Proven to perform, the Solvane Firmlift &amp; Glow facial renders your skin ultraluminous with a firmer, tighter, and more youthfully defined appearance.</p>
    </article>
  </section>

  <section class="column column--middle">
    <article class="service">
      <h2 class="service-title">Soothing Botanica<br>Treatment Facial</h2>
      <p class="service-price">$100 | 60 minutes</p>
      <p class="service-desc">This highly effective, soothing treatment calms redness and alleviates irritated or sensitive skin. A healing Propolis ampoule (natural ingredient collected by bees) is applied to desensitize the skin's surface and strengthen capillaries. A cooling liftoff mask is then applied to seal in the vitamin enriched beneficial ampoule.</p>
    </article>
    <article class="service">
      <h2 class="service-title">Radiance Phototherapy<br>Treatment</h2>
      <p class="service-price">$150 | Package 8/$800</p>
      <p class="service-desc">Uses heat and light energy to gently break up areas of excess pigment while stimulating the production of new collagen. Improved skin tone, less spots, fewer pink areas, less redness, reduction in fine lines and wrinkles. Diminishes pores and restores natural radiant glow of skin. Like laser treatments MicroPhotoTherapy treats skin with therapeutic light energy but unlike laser treatments, Micro PhotoTherapy features gentle waves of heat and light that improve the skin with no downtime and very little discomfort. We recommend 8 treatments 1 to 2 times a week for best results.</p>
    </article>
  </section>

  <section class="column column--right">
    <article class="service">
      <h2 class="service-title">Diamond<br>Microdermabrasion<br>Treatment</h2>
      <p class="service-price">$78</p>
      <p class="service-desc">With this treatment you will see softening of fine lines and wrinkles and smoothing of coarsely textured skin. Dull, stressed or congested skin will be brighter and clearer. The appearance of enlarged pores, and acne scars will be minimized. Your at home products will be able to penetrate deeper therefore, are more effective. Or add this to any facial or most peels for just $30.</p>
    </article>
  </section>

  <p class="brand">Velora<span class="brand-tag">Lash &amp; Skin Spa</span></p>
</main>
</body>
</html>
```